Stationary for Beauty and Spa School

Create a business card, letterhead and envelopes (primarily #10 envelope with and without window and catalog envelope) for a beauty and wellness school in Miami, Fl. We offer 8 different programs of study and need an eye catching look. Looking for a combination of modern yet sophisticated. Nothing corporate or business looking. Would like to have a look and feel that is similar (or incorporates aspects) of a new website we will be launching in the next 30 days (screen shot attached.)

The final design should communicate style and elegance in a down to earth and friendly way. We strive to provide our students with quality education, friendly and amicable staff and experienced instructors.
Updates

Hello. FYI, in order to print an aesthetically appealing business card, we would like to print them (the business cards) using silk printing method, with spot UV coating (on some elements, maybe the logo, or depending on the design) and die cuts. Please think of this when preparing your design.

Only 1 day left, please submit your designs for selection. Thanks

Target Market(s)

Adults 18-49 years who are mostly interested in beauty and fashion. Need a youthful & modern look, yet sophisticated and elegant.

Industry/Entity Type

School

Colors
e34197
6b449b
add136
f79021

Requirements
Must have
• Similar look and feel as website (see attached screen shot)
Same look and feel of website (see attached screenshot)
Logo
Address: 5216 SW 3rd Avenue. Miami, Fl 33155
Telephone: 305-514-9382
Fax: 786-420-5163
website/url: www.luminora.edu
incorporate Photo of blonde model (attached)
Nice to have
• Tag line: "Beautify your future." Also, maybe two-sided business card. Would be nice if we could mention our programs (maybe in the back of the card). Below are the program offerings (names cannot be changed but order is irrelevant)... Cosmetology, Barber, Spa Therapy, Massage Therapy, Makeup Artistry, Skin Care, Manicure, Pedicure & Nail Extensions, Full Specialist.

A design with text plus a beautiful photo of a model is appealing. Attached to the files is a sample of a cover for a student handbook we have created. You should use the photo of the blonde model (attached) in your design. The original (quality) version of this stock photograph has been uploaded.

Also would be nice to request clients to follow us on facebook and instagram by including the icons.
Should not have
• A corporate or business look. We are a vocational school teaching beauty and spa programs and we like our advertising to have a look that resembles the industry. We do not want a very serious look or snobby feel.

```html
<!DOCTYPE html>
<html lang="en">
<head>
<meta charset="utf-8">
<title>Luminora School of Beauty – Business Card</title>
<link rel="stylesheet" href="https://fonts.googleapis.com/css2?family=Montserrat:wght@400;500;600;700&family=Ubuntu+Condensed&display=swap">
<style>
  :root {
    --bg: #d9d6d4;
    --card-black: #050505;
    --card-white: #ffffff;
    --pink: #c8208f;
    --pink-bright: #e34197;
    --orange: #f79021;
    --ink: #1a1a1a;
    --text-light: #f2f2f2;
    --muted: #444;
  }
  * { margin: 0; padding: 0; box-sizing: border-box; }
  html, body { width: 1200px; height: 960px; overflow: hidden; }
  body {
    background: var(--bg);
    position: relative;
    font-family: "Montserrat", sans-serif;
  }
  .card {
    position: absolute;
    left: 250px;
    width: 700px;
    height: 400px;
    box-shadow: 0 10px 28px rgba(0,0,0,0.25);
  }
  /* Card back: programs */
  .card-back {
    top: 60px;
    background: var(--card-black);
  }
  .ornament-area {
    position: absolute;
    left: 24px;
    top: 26px;
    width: 380px;
    height: 360px;
    border-radius: 40% 55% 30% 45%;
    background: radial-gradient(circle at 40% 55%, rgba(247,144,33,0.55), rgba(227,65,151,0.25) 45%, rgba(5,5,5,0) 72%);
  }
  .tagline {
    position: absolute;
    right: 58px;
    top: 58px;
    font-family: "Ubuntu Condensed", sans-serif;
    font-size: 27px;
    color: var(--pink-bright);
    letter-spacing: 0.5px;
  }
  .programs {
    position: absolute;
    right: 58px;
    top: 122px;
    list-style: none;
    text-align: right;
    font-family: "Ubuntu Condensed", sans-serif;
    font-size: 21px;
    line-height: 31px;
    color: var(--text-light);
  }
  /* Card front: contact */
  .card-front {
    top: 500px;
    background: var(--card-white);
  }
  .brand {
    position: absolute;
    right: 52px;
    top: 38px;
    text-align: right;
    color: var(--ink);
    font-weight: 600;
  }
  .brand-name { font-size: 46px; letter-spacing: 1px; line-height: 1; }
  .brand-sub { font-size: 15px; letter-spacing: 1.2px; margin-top: 6px; }
  .contact {
    position: absolute;
    left: 50px;
    top: 110px;
  }
  .person-name {
    font-size: 18px;
    font-weight: 700;
    color: var(--pink);
    letter-spacing: 1px;
  }
  .person-role {
    font-size: 13px;
    font-weight: 600;
    color: var(--ink);
    margin-bottom: 22px;
  }
  .address {
    font-size: 13.5px;
    color: var(--ink);
    letter-spacing: 0.6px;
    margin-bottom: 10px;
  }
  .contact-list { list-style: none; }
  .contact-list li {
    display: flex;
    align-items: center;
    gap: 12px;
    font-size: 14px;
    color: var(--ink);
    letter-spacing: 0.6px;
    line-height: 20px;
  }
  .contact-list svg { width: 14px; height: 14px; flex: none; }
  .follow {
    position: absolute;
    right: 52px;
    bottom: 40px;
    display: flex;
    align-items: center;
    gap: 10px;
    font-size: 10px;
    color: var(--muted);
    letter-spacing: 0.5px;
  }
  .social-square {
    width: 28px;
    height: 24px;
    border-radius: 3px;
  }
  .social-square.one { background: #3b5998; }
  .social-square.two { background: #8a6a4f; }
</style>
</head>
<body>

  <section class="card card-back">
    <div class="ornament-area" role="img" aria-label="Orange and pink swirling floral ornament with concentric circle blossoms"></div>
    <p class="tagline">~ BEAUTIFY YOUR FUTURE ~</p>
    <ul class="programs">
      <li>Cosmetology | Barber | Spa Therapy</li>
      <li>Massage Therapy | Makeup Artistry</li>
      <li>Pedicure &amp; Nail Extensions</li>
      <li>Skin Care | Manicure</li>
    </ul>
  </section>

  <section class="card card-front">
    <div class="brand">
      <div class="brand-name">Luminora</div>
      <div class="brand-sub">SCHOOL OF BEAUTY</div>
    </div>

    <div class="contact">
      <p class="person-name">ELENA RUIZ</p>
      <p class="person-role">President</p>
      <p class="address">5216 SW 3rd Avenue. Miami, Fl 33155</p>
      <ul class="contact-list">
        <li>
          <svg viewBox="0 0 16 16" aria-hidden="true"><path fill="#e34197" d="M1 6c0-2 3-3 7-3s7 1 7 3v1h-3V5.5C11 5 9.5 4.8 8 4.8S5 5 4 5.5V7H1z"/><path fill="#e34197" d="M4 8h8l2 6H2z"/><circle cx="8" cy="11" r="1.6" fill="#fff"/></svg>
          305-514-9382
        </li>
        <li>
          <svg viewBox="0 0 16 16" aria-hidden="true"><rect x="4" y="1.5" width="8" height="4" fill="#e34197"/><rect x="1" y="6" width="14" height="6" rx="1.5" fill="#e34197"/><rect x="4" y="10" width="8" height="4.5" fill="#e34197" stroke="#fff" stroke-width="1"/></svg>
          786-420-5163
        </li>
        <li>
          <svg viewBox="0 0 16 16" aria-hidden="true"><g fill="none" stroke="#e34197" stroke-width="1.2"><circle cx="8" cy="8" r="6.5"/><ellipse cx="8" cy="8" rx="3" ry="6.5"/><path d="M1.5 8h13M2.5 4.8h11M2.5 11.2h11"/></g></svg>
          www.luminora.edu
        </li>
      </ul>
    </div>

    <div class="follow">
      <span>Follow Us:</span>
      <span class="social-square one"></span>
      <span class="social-square two"></span>
    </div>
  </section>

</body>
</html>
```